"Retire With The Harrowgate Fund" Book Cover Design

This book is 5.5 x. 8.5 in size. Not enough room for any writing on the spine either. About 100 pages, and 18,000 words max.
The Harrowgate Fund goes back to 1930. In this book, I run scenario after scenario seeing what the best strategy was for someone to Retire With The Harrowgate Fund and never run out of money. And how they MIGHT be able to use this info to build a solid retirement plan using the Harrowgate Fund for themselves.
Target Market(s)
Soon-to-be and recent middle-class, married retirees.
Industry/Entity Type
Investment Advisory
Requirements
Must have
- MUST BE EYE CATCHING!
Should not have
- No Piggy Banks or old people sitting on a beach or any yachts.

```html
<!DOCTYPE html>
<html lang="en">
<head>
<meta charset="utf-8">
<title>Retire With The Harrowgate Fund — Book Cover</title>
<link rel="stylesheet" href="https://fonts.googleapis.com/css2?family=Montserrat:wght@300;700;800&family=Arvo:wght@700&display=swap">
<style>
  :root {
    --page: #ffffff;
    --sky: #0afcd4;
    --ink: #0e0e0e;
    --orange: #ff6a00;
    --yellow: #f9ff00;
    --cloud: #ffffff;
    --author: #ffffff;
  }
  html, body {
    margin: 0;
    padding: 0;
    width: 1200px;
    height: 1200px;
    overflow: hidden;
    background: var(--page);
  }
  .canvas {
    position: relative;
    width: 1200px;
    height: 1200px;
  }
  .book-cover {
    position: absolute;
    left: 254px;
    top: 67px;
    width: 691px;
    height: 1066px;
    display: block;
  }
  .cover-sky { fill: var(--sky); }
  .title-lead {
    font-family: "Montserrat", sans-serif;
    font-weight: 300;
    font-size: 96px;
    fill: var(--ink);
  }
  .title-name {
    font-family: "Montserrat", sans-serif;
    font-weight: 800;
    font-size: 118px;
    fill: var(--ink);
  }
  .title-fund {
    font-family: "Montserrat", sans-serif;
    font-weight: 700;
    font-size: 316px;
    fill: var(--ink);
  }
  .author-name {
    font-family: "Arvo", serif;
    font-weight: 700;
    font-size: 72px;
    fill: var(--author);
    letter-spacing: 3px;
  }
</style>
</head>
<body>
<main class="canvas">
  <svg class="book-cover" viewBox="0 0 1037 1600" xmlns="http://www.w3.org/2000/svg" aria-label="Book cover: Retire With The Harrowgate Fund">
    <defs>
      <linearGradient id="cloudsFade" x1="0" y1="0" x2="0" y2="1">
        <stop offset="0" stop-color="var(--cloud)" stop-opacity="0.9"/>
        <stop offset="0.6" stop-color="var(--cloud)" stop-opacity="0.75"/>
        <stop offset="1" stop-color="var(--cloud)" stop-opacity="0"/>
      </linearGradient>
      <linearGradient id="barF" gradientUnits="userSpaceOnUse" x1="0" y1="973" x2="0" y2="1600">
        <stop offset="0" stop-color="var(--orange)"/>
        <stop offset="0.36" stop-color="var(--yellow)"/>
        <stop offset="0.7" stop-color="var(--orange)"/>
        <stop offset="1" stop-color="var(--orange)"/>
      </linearGradient>
      <linearGradient id="barU" gradientUnits="userSpaceOnUse" x1="0" y1="960" x2="0" y2="1600">
        <stop offset="0" stop-color="var(--orange)"/>
        <stop offset="0.3" stop-color="var(--yellow)"/>
        <stop offset="0.62" stop-color="var(--orange)"/>
        <stop offset="1" stop-color="var(--orange)"/>
      </linearGradient>
      <linearGradient id="barN" gradientUnits="userSpaceOnUse" x1="0" y1="900" x2="0" y2="1600">
        <stop offset="0" stop-color="var(--orange)"/>
        <stop offset="0.3" stop-color="var(--yellow)"/>
        <stop offset="0.6" stop-color="var(--orange)"/>
        <stop offset="1" stop-color="var(--orange)"/>
      </linearGradient>
      <linearGradient id="barD" gradientUnits="userSpaceOnUse" x1="0" y1="880" x2="0" y2="1600">
        <stop offset="0" stop-color="var(--orange)"/>
        <stop offset="0.3" stop-color="var(--yellow)"/>
        <stop offset="0.58" stop-color="var(--orange)"/>
        <stop offset="1" stop-color="var(--orange)"/>
      </linearGradient>
      <filter id="authorShadow" x="-10%" y="-40%" width="120%" height="180%">
        <feDropShadow dx="3" dy="6" stdDeviation="6" flood-color="#3a1a00" flood-opacity="0.7"/>
      </filter>
    </defs>

    <rect class="cover-sky" x="0" y="0" width="1037" height="1600"/>

    <rect class="cover-clouds" x="120" y="0" width="917" height="460" rx="80" fill="url(#cloudsFade)" role="img" aria-label="Paper-cut white clouds drifting across the sky"/>

    <g class="fund-bars">
      <rect x="62" y="960" width="39" height="640" fill="url(#barF)"/>
      <rect x="259" y="900" width="180" height="700" fill="url(#barU)"/>
      <rect x="505" y="900" width="201" height="700" fill="url(#barN)"/>
      <rect x="773" y="880" width="201" height="720" fill="url(#barD)"/>
    </g>

    <text class="title-lead" x="70" y="548" textLength="892" lengthAdjust="spacingAndGlyphs">RETIRE WITH THE</text>
    <text class="title-name" x="60" y="692" textLength="918" lengthAdjust="spacingAndGlyphs">HARROWGATE</text>
    <text class="title-fund" x="56" y="973" textLength="920" lengthAdjust="spacingAndGlyphs">FUND</text>

    <text class="author-name" x="515" y="1474" text-anchor="middle" filter="url(#authorShadow)">Author´s Name</text>
  </svg>
</main>
</body>
</html>
```